vorbo.com music website

I need a graphic designer to help me design a very modern looking theme for vorbo.com, a website for sharing songs. I currently have a very ugly old-looking design that I want to replace. I need a great logo, a great page theme. Just one comp is all I need of the home page. Must have two tag lines: "it pays to share" and "get paid to share music" The current design has all the elements I need, so I have attached it as a download. vorbo is pronounced vorboh. the current site is not live. Please feel free to send me questions.

Reason: I want to give everyone a chance to get their design in. Thank you.

Target Market(s)

The site needs to appeal to music fans that will be pulled in by the concept of "it pays to share," as well as the pop of the design. It has to look fun and cool. Empahsis on modern looking design.

Industry/Entity Type

Graphic Designer

Requirements
Must have
• engaging logo, there must be a container that holds video, scrolls right and left. 6 action buttons, for Linkrally, Quipster, My, Add, Search, More. You can put the first letter only on the buttons. Must have two tag lines: "it pays to share" and "get paid to share music" Please include the elements, such as login, join, etc... that are in the comp that you can download. Obviously I don't want it to look like what I already have, except that it must have a container that holds the video. The container that holds the video has to have the same aspect ratio that clipvista uses for it's embed codes. You can find this ratio by checking any clipvista video embed code, they have a custom size tool which lets you play with the sizes. Any question, pls contact thanks.
Nice to have
• unlike the existing comp, it can have white space. Just looking for a good modern theme with a cool logo. Jquery style themes might be nice... Also, think along the lines of a cool techy feel for mobile...

This is a cool image, but obviously don't get too close to it because it belongs to another music site:

http://mxnewsdesk2011.files.blogvane.example/2012/03/screen-shot-2012-03-28-at-12-02-36-pm.png?w=194

```html
<!DOCTYPE html>
<html lang="en">
<head>
<meta charset="utf-8">
<title>vorbo – It Pays To Share</title>
<link rel="stylesheet" href="https://fonts.googleapis.com/css2?family=Questrial&family=Poppins:wght@600;700&family=Varela+Round&family=Roboto:ital,wght@0,700;1,400&display=swap">
<style>
  :root {
    --bg-dark: #2f3337;
    --bg-dark-2: #3c4247;
    --accent-blue: #4ab0e2;
    --link-blue: #57acd8;
    --login-blue: #3d8fb8;
    --orange: #f47a43;
    --orange-dark: #d9622e;
    --white: #ffffff;
    --text-dark: #111111;
    --frame-light: #cfd0d1;
    --frame-dark: #2a2c2e;
    --stat-grey: #8e959b;
  }
  * { margin: 0; padding: 0; box-sizing: border-box; }
  html, body { width: 1200px; height: 1134px; overflow: hidden; }
  body { position: relative; background: var(--white); font-family: "Questrial", sans-serif; }

  .hero-band {
    position: absolute; left: 0; top: 0; width: 1200px; height: 624px;
    background: radial-gradient(ellipse 420px 260px at 600px 250px, #5b6570 0%, var(--bg-dark-2) 45%, var(--bg-dark) 100%);
    border-top: 4px solid var(--login-blue);
  }
  .hero-shadow {
    position: absolute; left: 0; top: 624px; width: 1200px; height: 70px;
    background: linear-gradient(#b9bcbf, #ffffff);
  }

  .utility-nav { position: absolute; top: 4px; right: 126px; display: flex; height: 33px; }
  .utility-nav a {
    display: block; padding: 0 16px; line-height: 33px; font-size: 14px;
    color: var(--link-blue); text-decoration: none; letter-spacing: .3px;
  }
  .utility-nav a.account { background: var(--login-blue); color: var(--white); }

  .brand {
    position: absolute; left: 138px; top: 26px;
    font-family: "Varela Round", sans-serif; font-size: 74px; line-height: 1;
    color: var(--accent-blue); letter-spacing: -1px;
  }

  .main-nav { position: absolute; top: 82px; right: 126px; display: flex; gap: 46px; }
  .main-nav a { color: var(--white); text-decoration: none; font-size: 20px; letter-spacing: .5px; }

  .tagline {
    position: absolute; top: 132px; left: 0; width: 1200px; text-align: center;
    color: var(--white); font-size: 37px; font-weight: 400; letter-spacing: .5px;
  }

  .stats { position: absolute; top: 247px; left: 282px; display: flex; gap: 22px;
    font-family: "Roboto", sans-serif; font-style: italic; font-size: 12px; color: var(--stat-grey); }
  .stats em { color: var(--link-blue); }

  .download {
    position: absolute; left: 802px; top: 212px; width: 118px; height: 47px;
  }

  .side-slide {
    position: absolute; top: 366px; width: 156px; height: 222px;
    border: 5px solid var(--frame-light);
  }
  .side-slide.left { left: 127px; background: linear-gradient(135deg, #6b5a52, #c9b8ae 55%, #8d3b33); }
  .side-slide.right { left: 918px; background: linear-gradient(135deg, #d7d5d6, #7a6b6a 50%, #3a3434); }
  .chevron { position: absolute; top: 440px; width: 50px; height: 84px; }
  .chevron.prev { left: 168px; }
  .chevron.next { left: 968px; }

  .video-player {
    position: absolute; left: 282px; top: 280px; width: 638px; height: 406px;
    background: linear-gradient(var(--frame-dark) 0%, var(--frame-dark) 60%, var(--frame-light) 80%, #e3e3e3 100%);
    padding: 9px 10px 10px 10px;
    box-shadow: 0 14px 18px -10px rgba(0,0,0,.45);
  }
  .video-still {
    position: relative; width: 618px; height: 387px;
    background: radial-gradient(ellipse at 72% 40%, #8b6a55 0%, #4d3428 45%, #1d1411 100%);
  }
  .play-button { position: absolute; left: 245px; top: 128px; width: 128px; height: 128px; }

  .song-title {
    position: absolute; top: 700px; left: 0; width: 1200px; text-align: center;
    font-family: "Poppins", sans-serif; font-weight: 700; font-size: 28px; color: var(--text-dark);
  }

  .skyline {
    position: absolute; left: 0; top: 776px; width: 1200px; height: 148px;
    background: linear-gradient(rgba(47,51,55,0) 0%, rgba(47,51,55,.55) 45%, var(--bg-dark) 100%);
  }
  .footer-band {
    position: absolute; left: 0; top: 924px; width: 1200px; height: 210px;
    background: radial-gradient(ellipse 420px 200px at 600px 1090px, #4a5158 0%, var(--bg-dark) 100%);
  }

  .cta {
    position: absolute; left: 329px; top: 919px; width: 542px; height: 67px;
    background: var(--orange); color: var(--white); text-align: center;
    font-size: 36px; line-height: 67px; letter-spacing: .3px; text-decoration: none;
    box-shadow: 0 10px 12px -8px rgba(0,0,0,.6);
  }

  .social { position: absolute; top: 1020px; left: 461px; display: flex; gap: 10px; }
  .social a {
    display: block; width: 38px; height: 38px; border-radius: 7px;
    border: 2px solid #d7dadd; color: var(--white); text-decoration: none;
    font-family: "Roboto", sans-serif; font-weight: 700; font-size: 18px;
    line-height: 34px; text-align: center;
  }
  .social .linkrally { background: #3b5ea8; }
  .social .quipster { background: #3fb2e3; }
  .social .pickly { background: #2f67a8; }
  .social .postwell { background: #f2782f; }
  .social .tunelog { background: #c9252a; }
  .social .clipvista { background: #f4f4f4; color: #c4302b; }

  .copyright {
    position: absolute; top: 1085px; left: 0; width: 1200px; text-align: center;
    font-family: "Roboto", sans-serif; font-size: 12px; color: var(--white);
  }
</style>
</head>
<body>
  <div class="hero-band"></div>
  <div class="hero-shadow"></div>

  <nav class="utility-nav">
    <a href="#">TERMS</a>
    <a href="#">PRIVACY</a>
    <a href="#">SUPPORT</a>
    <a href="#" class="account">LOGIN</a>
    <a href="#" class="account">JOIN</a>
  </nav>

  <div class="brand">vorbo</div>

  <nav class="main-nav">
    <a href="#">HOME</a>
    <a href="#">ABOUT</a>
    <a href="#">SETTINGS</a>
  </nav>

  <h1 class="tagline">IT PAYS TO SHARE</h1>

  <div class="stats">
    <span>10,456 <em>Vorbos</em></span>
    <span>11,223 <em>Fans</em></span>
  </div>

  <svg class="download" viewBox="0 0 118 47" aria-label="Download">
    <polygon points="0,0 10,10 0,10" fill="var(--orange-dark)"/>
    <rect x="0" y="10" width="118" height="37" fill="var(--orange)"/>
    <g fill="#fff">
      <rect x="13" y="32" width="14" height="3"/>
      <rect x="13" y="29" width="2" height="4"/>
      <rect x="25" y="29" width="2" height="4"/>
      <rect x="18.5" y="18" width="3" height="8"/>
      <polygon points="15,24 25,24 20,30"/>
    </g>
    <text x="34" y="34" fill="#fff" font-family="Roboto, sans-serif" font-weight="700" font-size="16">Download</text>
  </svg>

  <div class="side-slide left" role="img" aria-label="Previous video thumbnail: performers on stage"></div>
  <div class="side-slide right" role="img" aria-label="Next video thumbnail: group of young music fans"></div>

  <svg class="chevron prev" viewBox="0 0 50 84" aria-label="Previous">
    <polygon points="50,0 30,0 0,42 30,84 50,84 20,42" fill="#fff"/>
  </svg>
  <svg class="chevron next" viewBox="0 0 50 84" aria-label="Next">
    <polygon points="0,0 20,0 50,42 20,84 0,84 30,42" fill="#fff"/>
  </svg>

  <div class="video-player">
    <div class="video-still" role="img" aria-label="Video still: singer in a hat at a studio microphone">
      <svg class="play-button" viewBox="0 0 128 128" aria-label="Play">
        <circle cx="64" cy="64" r="64" fill="rgba(40,40,40,.7)"/>
        <polygon points="52,30 86,64 52,98" fill="#9a9a9a"/>
      </svg>
    </div>
  </div>

  <h2 class="song-title">Velvet Orbitae</h2>

  <div class="skyline" role="img" aria-label="City skyline silhouette"></div>
  <div class="footer-band"></div>

  <a href="#" class="cta">GET PAID TO SHARE MUSIC</a>

  <div class="social">
    <a href="#" class="linkrally" aria-label="Linkrally">L</a>
    <a href="#" class="quipster" aria-label="Quipster">Q</a>
    <a href="#" class="pickly" aria-label="Pickly">P</a>
    <a href="#" class="postwell" aria-label="Postwell">P</a>
    <a href="#" class="tunelog" aria-label="Tunelog">T</a>
    <a href="#" class="clipvista" aria-label="clipvista">C</a>
  </div>

  <p class="copyright">© 2012 Kinship Share Media. All Rights Reserved.</p>
</body>
</html>
```